Business card design needed

We need something on the back that allows the customer to get five stamps then the sixth visit they get 25 dollars to spend.
Industry/Entity Type
Business
Contact Information for Business Card
Quality meat,value for money,spit roast hire, wholesale pubs clubs,cater for bbqs.marlow lane butchery 217 marlow lane.64739204.

```html
<!DOCTYPE html>
<html lang="en">
<head>
<meta charset="utf-8">
<title>Marlow Lane Butchery – Business Card</title>
<link href="https://fonts.googleapis.com/css2?family=Kalam:wght@400;700&family=Arimo:ital,wght@1,700&display=swap" rel="stylesheet">
<style>
  :root {
    --page: #ffffff;
    --kraft: #c8a983;
    --kraft-light: #d9c09d;
    --kraft-edge: #a5835f;
    --ink-red: #7d1d1f;
    --ink-brown: #4f221c;
    --butcher-red: #c9272b;
    --butcher-deep: #8e1d1f;
  }
  * { margin: 0; padding: 0; box-sizing: border-box; }
  html, body { width: 1177px; height: 1200px; overflow: hidden; background: var(--page); }
  .canvas { position: relative; width: 1177px; height: 1200px; }

  .card {
    position: absolute;
    background: radial-gradient(ellipse at 50% 45%, var(--kraft-light) 0%, var(--kraft) 60%, var(--kraft-edge) 100%);
    overflow: hidden;
  }
  .card--front { left: 57px; top: 44px; width: 752px; height: 464px; }
  .card--back  { left: 362px; top: 654px; width: 761px; height: 469px; }

  .illustration {
    position: absolute;
    background: linear-gradient(160deg, var(--butcher-deep) 0%, var(--butcher-red) 70%, #e8342f 100%);
    border-radius: 6px;
    opacity: 0.85;
  }
  .card--front .illustration { left: 12px; top: 8px; width: 252px; height: 310px; }
  .card--back .illustration  { left: 8px; top: 8px; width: 170px; height: 200px; }

  .brand-name {
    position: absolute;
    font-family: "Kalam", cursive;
    font-weight: 700;
    color: var(--ink-red);
    text-align: center;
    line-height: 1;
  }
  .card--front .brand-name { left: 207px; top: 22px; width: 530px; font-size: 60px; }
  .card--back .brand-name  { left: 200px; top: 18px; width: 440px; font-size: 50px; }

  .contact {
    position: absolute;
    left: 250px; top: 190px; width: 480px;
    font-family: "Arimo", Arial, sans-serif;
    font-style: italic; font-weight: 700;
    color: var(--ink-red);
    font-size: 25px;
    line-height: 34px;
  }
  .contact span { display: block; }
  .contact .address { padding-left: 127px; }
  .contact .phone   { padding-left: 153px; }
  .contact .mobile  { padding-left: 50px; }
  .contact .email   { padding-left: 14px; }

  .services {
    position: absolute;
    left: 40px; top: 360px; width: 690px;
    font-family: "Kalam", cursive;
    color: var(--ink-brown);
    font-size: 30px;
    line-height: 36px;
    text-align: center;
  }
  .services .lead {
    position: absolute; left: 0; top: 0;
    transform: rotate(-14deg);
    transform-origin: left bottom;
  }
  .services .line1 { display: block; padding-left: 60px; margin-top: 12px; }

  .offer {
    position: absolute;
    left: 100px; top: 140px; width: 620px;
    font-family: "Kalam", cursive;
    color: var(--ink-red);
    text-align: center;
    font-size: 28px;
    line-height: 32px;
  }
  .offer .note { font-size: 18px; color: var(--ink-brown); margin-top: 4px; }

  .stamp-grid { position: absolute; left: 0; top: 0; width: 761px; height: 469px; }
  .stamp-grid line { stroke: var(--ink-brown); }

  .reward {
    position: absolute;
    left: 612px; top: 305px; width: 104px; height: 104px;
    border: 4px solid var(--ink-brown);
    border-radius: 50%;
    font-family: "Kalam", cursive; font-weight: 700;
    color: var(--ink-brown);
    display: flex; flex-direction: column; align-items: center; justify-content: center;
    transform: rotate(-12deg);
    line-height: 1;
    opacity: 0.85;
  }
  .reward .free { font-size: 20px; }
  .reward .amount { font-size: 40px; }
</style>
</head>
<body>
<div class="canvas">

  <section class="card card--front">
    <div class="illustration" role="img" aria-label="Red illustration of a butcher holding a leg of meat above crossed cleaver and knife"></div>
    <h1 class="brand-name">Marlow lane<br>Butchery</h1>
    <address class="contact">
      <span class="address">217 marlow lane</span>
      <span class="phone">0264739204</span>
      <span class="mobile">Mobile - 0491570156</span>
      <span class="email">marlowlnbutchery@mailhub.com</span>
    </address>
    <p class="services">
      <span class="lead">Quality</span>
      <span class="line1">meat,value for money,spit roast hire, wholesale</span>
      pubs clubs,cater for bbqs.
    </p>
  </section>

  <section class="card card--back">
    <div class="illustration" role="img" aria-label="Red illustration of a butcher holding a leg of meat above crossed cleaver and knife"></div>
    <h2 class="brand-name">Marlow lane<br>Butchery</h2>
    <div class="offer">
      <p>spend $50 or more to recieve a stamp</p>
      <p>&amp;</p>
      <p>recieve $25 off your 6th visit!</p>
      <p class="note">(excludes meat packs)</p>
    </div>
    <svg class="stamp-grid" viewBox="0 0 761 469" aria-hidden="true">
      <line x1="11" y1="290" x2="750" y2="290" stroke-width="6"/>
      <line x1="21" y1="290" x2="21" y2="439" stroke-width="5"/>
      <line x1="142" y1="290" x2="142" y2="439" stroke-width="5"/>
      <line x1="257" y1="290" x2="257" y2="439" stroke-width="5"/>
      <line x1="374" y1="290" x2="374" y2="439" stroke-width="5"/>
      <line x1="489" y1="290" x2="489" y2="439" stroke-width="5"/>
      <line x1="604" y1="290" x2="604" y2="439" stroke-width="5"/>
      <line x1="740" y1="290" x2="740" y2="439" stroke-width="5"/>
    </svg>
    <div class="reward">
      <span class="free">FREE</span>
      <span class="amount">$25</span>
    </div>
  </section>

</div>
</body>
</html>
```